Web Design Project for Velorasa cloud based service

None of us is a designer, and ENGLISH is not our first language, but we need to make sure that those bidding for this project understand that we're just looking for the creative components in order to build a website and we don't need you to create all the pages and /or diagram the website for us. Please ask as many questions as you want for us to ensure we don't waste your time.

Content and Community Management System
- We need a redesign of the Back Office Screens
o The kind of screen detailed on the (file 2 attached bellow) “Velorasa Some Screens.pptx”
- Following, as a strong reference te velorasa logo design line (file 1 attached bellow)
- We DO NOT need application, or implementation, only the following SOW.

Scope of Work (SOW) by components that we need:
- Main Theme
- Tables
- Buttons
- Icons
- Lists
- Form elements

OUT of Scope (we DO NOT need it):
· Emerging Windows implementation (jquery – lightbox)
· Layout (we do not need you to create the layout for us)
· Module Development (Css 3, jQuery, Html 5)

Reason: We're extending the deadline in order to have more options to select. The current option do not fit our expectation yet. Any question, please do it. Many thanks. Velorasa Team.

Hi designers!

We've [a] extended the deadline in order to have more choices and we made a change on the Power Point file attached with [b] the 3 most important screen than include all the components/element we need designed from you.

We wait for your proposal.
Let's do it!

Many Thanks.
Best regards.

velorasa Team.

```html
<!DOCTYPE html>
<html lang="en">
<head>
<meta charset="utf-8">
<title>Velorasa – Plantillas</title>
<link rel="stylesheet" href="https://fonts.googleapis.com/css2?family=Source+Sans+3:wght@400;600;700&display=swap">
<style>
  :root {
    --page-bg: #ededed;
    --glow: #ffffff;
    --panel: #ffffff;
    --bar: #dedede;
    --ink: #333333;
    --muted: #6a6a6a;
    --accent: #e0490c;
    --link: #b3400e;
    --row-top: #fff4f0;
    --row-bottom: #fbd9cd;
    --row-line: #f2c2b1;
    --note-bg: #f2f2f2;
    --note-line: #d9d9d9;
    --k: 1.171875;
  }
  * { box-sizing: border-box; margin: 0; padding: 0; }
  html, body { width: 1200px; height: 752px; overflow: hidden; }
  body {
    background: var(--page-bg);
    font-family: "Source Sans 3", "Myriad Pro", Arial, sans-serif;
    color: var(--ink);
  }
  .stage {
    position: relative;
    width: 1024px; height: 642px;
    transform: scale(var(--k));
    transform-origin: 0 0;
    background:
      radial-gradient(circle at 110px 90px, var(--glow) 0, rgba(255,255,255,.7) 90px, rgba(255,255,255,0) 200px),
      var(--page-bg);
  }
  a { color: var(--link); text-decoration: underline; }

  /* brand */
  .brand { position: absolute; left: 57px; top: 60px; display: flex; align-items: center; gap: 10px; }
  .brand-mark { width: 26px; height: 26px; background: var(--accent); }
  .brand-name { font-size: 24px; font-weight: 700; letter-spacing: .5px; color: #1b1b1b; text-transform: uppercase; }

  /* navigation */
  .main-nav { position: absolute; left: 0; top: 0; width: 100%; height: 0; }
  .nav-item {
    position: absolute; transform: translateX(-50%);
    font-size: 13px; color: var(--ink); white-space: nowrap; line-height: 31px;
  }
  .nav-item.is-active {
    background: var(--accent); color: #fff; width: 100px; text-align: center;
    border: 1px solid #c93e06;
  }

  /* content panel */
  .panel { position: absolute; left: 30px; top: 180px; width: 960px; height: 462px; background: var(--panel); }
  .context-bar {
    height: 42px; background: var(--bar); display: flex; align-items: center;
    justify-content: space-between; padding: 0 38px 0 24px; border-bottom: 1px solid #d2d2d2;
  }
  .context-title { font-size: 15px; color: var(--ink); }
  .user-links { font-size: 12.5px; color: var(--ink); }
  .user-links .sep { color: #888; margin: 0 5px; }

  /* sidebar */
  .sidebar { position: absolute; left: 23px; top: 72px; width: 196px; }
  .sidebar-title { font-size: 13px; color: var(--muted); margin-bottom: 14px; padding-left: 3px; }
  .property-list { list-style: none; }
  .property-list li { display: flex; align-items: flex-start; gap: 8px; height: 33px; padding-left: 4px; }
  .property-list a { font-size: 12.5px; display: block; width: 143px; padding-bottom: 9px; border-bottom: 1px dotted #d88a6b; }
  .property-list li:last-child a { border-bottom: none; }
  .doc-icon { width: 16px; height: 20px; flex: none; margin-top: -2px; }
  .note {
    position: absolute; left: 0; top: 231px; width: 196px; height: 87px;
    background: var(--note-bg); border: 1px solid var(--note-line);
    padding: 10px 18px; font-size: 12.5px; line-height: 20px; color: #444;
  }
  .note-links { margin-top: 7px; }

  /* table */
  .templates { position: absolute; left: 240px; top: 62px; width: 692px; }
  .templates h1 { font-size: 21px; font-weight: 400; color: #111; margin-bottom: 13px; }
  .data-table { width: 100%; border-collapse: collapse; font-size: 12.5px; }
  .data-table th {
    background: var(--accent); color: #fff; font-weight: 400; font-size: 13px;
    text-align: left; height: 31px; padding: 0;
  }
  .data-table td {
    vertical-align: top; padding: 18px 0 0; height: 66px; line-height: 17px;
    background: linear-gradient(var(--row-top), var(--row-bottom));
    border-bottom: 1px solid var(--row-line);
  }
  .col-name { width: 158px; padding-left: 24px !important; }
  .col-member { width: 138px; }
  .col-theme { width: 136px; }
  .col-address { width: 167px; }
  .name-cell { display: flex; gap: 8px; padding-left: 19px !important; }
  .name-cell .doc-icon { margin-top: 2px; }
</style>
</head>
<body>
<svg width="0" height="0" style="position:absolute" aria-hidden="true">
  <defs>
    <symbol id="doc" viewBox="0 0 16 20">
      <path d="M1 1h9l5 5v13H1z" fill="#fff" stroke="#c9c9c9"/>
      <path d="M10 1v5h5" fill="#f3b59c" stroke="#e0905f"/>
    </symbol>
  </defs>
</svg>

<div class="stage">
  <div class="brand">
    <span class="brand-mark"></span>
    <span class="brand-name">Velorasa</span>
  </div>

  <nav class="main-nav">
    <a class="nav-item" style="left:333px;top:62px;text-decoration:none">Company</a>
    <a class="nav-item is-active" style="left:447px;top:62px;text-decoration:none">About Us</a>
    <a class="nav-item" style="left:563px;top:62px;text-decoration:none">Testimonials</a>
    <a class="nav-item" style="left:681px;top:62px;text-decoration:none">Modules</a>
    <a class="nav-item" style="left:803px;top:62px;text-decoration:none">Adminstrative</a>
    <a class="nav-item" style="left:928px;top:62px;text-decoration:none">Live Store</a>
    <a class="nav-item" style="left:333px;top:111px;text-decoration:none">Get In Touch</a>
    <a class="nav-item" style="left:450px;top:111px;text-decoration:none">Plantiles</a>
  </nav>

  <section class="panel">
    <header class="context-bar">
      <span class="context-title">Proyecto:Region: BRASIL</span>
      <span class="user-links">User admin <span class="sep">|</span> Profeceinces <span class="sep">|</span> Profile <span class="sep">|</span> Siler</span>
    </header>

    <aside class="sidebar">
      <h2 class="sidebar-title" style="font-weight:400">Properties</h2>
      <ul class="property-list">
        <li><svg class="doc-icon"><use href="#doc"/></svg><a>Total les Plattesers</a></li>
        <li><svg class="doc-icon"><use href="#doc"/></svg><a>DT-BR</a></li>
        <li><svg class="doc-icon"><use href="#doc"/></svg><a>DT-BR home RQ</a></li>
        <li><svg class="doc-icon"><use href="#doc"/></svg><a>DTH Region Telephon</a></li>
      </ul>
      <div class="note">
        <p>Serioucing is Pettles arrey<br>Pare</p>
        <p class="note-links">Disclimari | Eleminere</p>
      </div>
    </aside>

    <div class="templates">
      <h1>Plantillas</h1>
      <table class="data-table">
        <thead>
          <tr>
            <th class="col-name">Name</th>
            <th class="col-member">Memeber Care</th>
            <th class="col-theme">Theme</th>
            <th class="col-address">Address Reciept</th>
            <th>Dated</th>
          </tr>
        </thead>
        <tbody>
          <tr>
            <td class="name-cell"><svg class="doc-icon"><use href="#doc"/></svg><a>DT-BR</a></td>
            <td><a>011-08 Mastets</a></td>
            <td><a>them goes<br>here</a></td>
            <td><a>22 Palsten ulisting oca<br>Plasttes</a></td>
            <td><a>01 Mar 2011,<br>11:00 PM</a></td>
          </tr>
          <tr>
            <td class="name-cell"><svg class="doc-icon"><use href="#doc"/></svg><a>DT-BR</a></td>
            <td><a>011-08 Mastets</a></td>
            <td><a>them goes<br>here</a></td>
            <td><a>22 Palsten ulisting oca<br>Plasttes</a></td>
            <td><a>01 Mar 2011,<br>11:00 PM</a></td>
          </tr>
          <tr>
            <td class="name-cell"><svg class="doc-icon"><use href="#doc"/></svg><a>DT-BR</a></td>
            <td><a>011-08 Mastets</a></td>
            <td><a>them goes<br>here</a></td>
            <td><a>22 Palsten ulisting oca<br>Plasttes</a></td>
            <td><a>01 Mar 2011,<br>11:00 PM</a></td>
          </tr>
          <tr>
            <td class="name-cell"><svg class="doc-icon"><use href="#doc"/></svg><a>DT-BR</a></td>
            <td><a>011-08 Mastets</a></td>
            <td><a>them goes<br>here</a></td>
            <td><a>22 Palsten ulisting oca<br>Plasttes</a></td>
            <td><a>01 Mar 2011,<br>11:00 PM</a></td>
          </tr>
        </tbody>
      </table>
    </div>
  </section>
</div>
</body>
</html>
```